New & Improved QUIVEL Business Card

I would like a two sided business card one side dedicated to home automation (security camera installation, television & sound bar mounting (hidden wires optional) , sink installation, fireplace mounting, chandelier installation and one side dedicated to all electronic repairs, In ex: dorva watch repairs, computer, Zelt, laptop repairs, Marvo's, Velkora and etc.. Using the colors on this flyer. The phone number &email I want on both sides is (555) 013-2947 & Tech@Quivel.example. SAME COLOR AS THE FLYER ATTACHED.

Target Market(s)

EVERYONE.

Contact Information for Business Card

I would like a two sided business card one side dedicated to home automation (security camera installation, television & sound bar mounting (hidden wires optional) , sink installation, fireplace mounting, chandelier installation and one side dedicated to all electronic repairs, In ex: dorva watch repairs, computer, Zelt, laptop repairs, Marvo's, Velkora and etc.. Using the colors on this flyer. The phone number &email I want on both sides is (555) 013-2947 & Tech@Quivel.example

Requirements
Must have
• -TV MOUNTING
-HOME AUTOMATION
-SECURITY CAMERA INSTALLATION
-ALL ELECTRONIC REPAIRS
- (555) 013-2947
-Tech@Quivel.example
-SAME COLOR AS THE FLYER
Nice to have
• Same colors & concept as the flyer attached below.
Should not have
• DO NOT DO A DIFF COLOR I WANT SAME COLOR AS THE FLYER ATTACHED.

```html
<!DOCTYPE html>
<html lang="en">
<head>
<meta charset="utf-8">
<title>QUIVEL Business Card</title>
<link href="https://fonts.googleapis.com/css2?family=Open+Sans:wght@400;600;700&display=swap" rel="stylesheet">
<style>
:root{
  --pink:#e8449a;
  --pink-light:#f06bb0;
  --pink-deep:#d8358a;
  --ink:#1e1e20;
  --charcoal:#2a2a2d;
  --charcoal-dark:#141416;
  --paper:#ffffff;
  --mist:#e9e9eb;
  --grey:#bfc0c4;
  --stage:#dcdcdf;
}
*{margin:0;padding:0;box-sizing:border-box}
html,body{width:1200px;height:780px;overflow:hidden;background:var(--stage);font-family:"Open Sans",Arial,sans-serif}
.canvas{position:relative;width:1200px;height:780px}
.card{position:absolute;top:40px;width:400px;height:700px;overflow:hidden;box-shadow:0 10px 30px rgba(0,0,0,.25)}
.card--repairs{left:160px;background:var(--paper)}
.card--automation{left:640px;background:linear-gradient(160deg,#3a3a3e 0%,var(--charcoal) 40%,var(--charcoal-dark) 100%)}
.layer{position:absolute;inset:0}
.brand{position:absolute;left:0;right:0;text-align:center;font-family:"Open Sans",Arial,sans-serif;font-weight:600;letter-spacing:.22em}
.card--repairs .brand{top:132px;font-size:36px;color:var(--paper)}
.device-labels{position:absolute;top:206px;left:0;right:0;display:flex;justify-content:space-around;padding:0 24px;font-size:11px;font-weight:700;letter-spacing:.08em;color:rgba(255,255,255,.5)}
.device-frame{position:absolute;border:1.5px solid rgba(255,255,255,.22)}
.device-art{position:absolute;left:70px;top:262px;width:260px;height:150px;border-radius:6px;background:linear-gradient(180deg,#f4f4f5,#c9cacd)}
.pitch{position:absolute;top:438px;left:0;right:0;text-align:center;font-size:17px;line-height:1.2;font-weight:600;color:var(--ink);text-transform:uppercase}
.headline{position:absolute;top:500px;left:0;right:0;text-align:center;font-size:21px;font-weight:700;color:var(--pink);letter-spacing:.01em}
.phone-bar{position:absolute;left:22px;right:22px;top:540px;height:44px;border-radius:22px;background:linear-gradient(180deg,#3a3a3d,var(--ink));display:flex;align-items:center;justify-content:center;gap:10px;color:var(--pink);font-size:21px;font-weight:700}
.email-row{position:absolute;left:22px;right:22px;top:594px;height:40px;display:flex;align-items:center;justify-content:center;gap:10px;font-size:18px;color:var(--ink)}
.base-bar{position:absolute;left:22px;right:22px;top:640px;height:14px;border-radius:7px;background:var(--ink)}
.card--automation .brand{top:40px;font-size:44px;color:var(--pink)}
.service-title{position:absolute;top:108px;left:0;right:0;text-align:center;font-size:21px;font-weight:700;color:var(--paper);letter-spacing:.03em}
.service-list{position:absolute;top:158px;left:30px;right:20px;list-style:none}
.service-list li{display:flex;align-items:flex-start;gap:12px;color:var(--paper);font-size:18px;line-height:1.2;margin-bottom:16px}
.service-list svg{flex:none;margin-top:2px}
.thumbs{position:absolute;top:378px;left:18px;right:18px;display:flex;gap:10px}
.thumb{flex:1;height:86px;border-radius:5px;border:2px solid var(--paper);background:linear-gradient(180deg,#f1f1f2,#bdbec2);position:relative;overflow:hidden}
.thumb span{position:absolute;left:0;right:0;bottom:0;background:rgba(60,60,64,.75);color:var(--paper);font-size:8px;font-weight:600;text-align:center;padding:2px 0;letter-spacing:.04em}
.contact{position:absolute;left:26px;right:20px;display:flex;align-items:center;gap:10px;color:var(--paper)}
.contact--phone{top:606px;font-size:22px;font-weight:700}
.contact--email{top:648px;font-size:18px;font-weight:400}
</style>
</head>
<body>
<main class="canvas">

  <section class="card card--repairs">
    <svg class="layer" width="400" height="700" viewBox="0 0 400 700" aria-hidden="true">
      <rect x="0" y="0" width="400" height="340" fill="var(--pink)"/>
      <polygon points="0,0 230,0 0,250" fill="var(--pink-light)" opacity=".45"/>
      <polygon points="400,0 400,300 150,0" fill="var(--pink-deep)" opacity=".35"/>
      <polygon points="0,300 200,345 400,300 400,360 200,420 0,360" fill="var(--mist)"/>
      <polygon points="0,330 200,380 400,330 400,350 200,400 0,350" fill="var(--grey)"/>
      <polygon points="0,252 200,330 400,252 400,300 200,350 0,300" fill="var(--paper)"/>
      <polygon points="0,290 200,340 400,290 400,300 200,350 0,300" fill="var(--ink)" opacity=".85"/>
    </svg>
    <div class="device-frame" style="left:36px;top:50px;width:100px;height:62px"></div>
    <div class="device-frame" style="left:165px;top:44px;width:70px;height:72px"></div>
    <div class="device-frame" style="left:275px;top:40px;width:90px;height:78px"></div>
    <div class="brand">QUIVEL</div>
    <div class="device-labels"><span>LAPTOPS</span><span>MOBILES</span><span>TABLETS</span></div>
    <div class="device-art" role="img" aria-label="Monitor, laptop, tablets and phones with cracked screens awaiting repair"></div>
    <p class="pitch">For any repairs, we come to you,<br>with unbeatable prices</p>
    <p class="headline">ALL ELECTRONIC REPAIRS</p>
    <div class="phone-bar">
      <svg width="22" height="22" viewBox="0 0 24 24" aria-hidden="true"><path d="M6.6 10.8a15 15 0 0 0 6.6 6.6l2.2-2.2a1 1 0 0 1 1-.25 11.4 11.4 0 0 0 3.6.57 1 1 0 0 1 1 1V20a1 1 0 0 1-1 1A17 17 0 0 1 3 4a1 1 0 0 1 1-1h3.5a1 1 0 0 1 1 1c0 1.25.2 2.45.57 3.57a1 1 0 0 1-.25 1z" fill="var(--pink)"/></svg>
      <span>(555) 013-2947</span>
    </div>
    <div class="email-row">
      <svg width="20" height="16" viewBox="0 0 20 16" aria-hidden="true"><rect x="1" y="1" width="18" height="14" rx="1.5" fill="none" stroke="var(--ink)" stroke-width="1.8"/><path d="M1.5 2l8.5 7 8.5-7" fill="none" stroke="var(--ink)" stroke-width="1.8"/></svg>
      <span>Tech@Quivel.example</span>
    </div>
    <div class="base-bar"></div>
  </section>

  <section class="card card--automation">
    <svg class="layer" width="400" height="700" viewBox="0 0 400 700" aria-hidden="true">
      <polygon points="0,470 200,548 400,440 400,470 200,578 0,500" fill="var(--grey)"/>
      <polygon points="0,492 200,570 400,462 400,478 200,586 0,508" fill="var(--paper)"/>
      <polygon points="0,508 200,586 400,478 400,700 0,700" fill="var(--pink)"/>
      <polygon points="400,478 400,700 250,700" fill="var(--pink-deep)" opacity=".4"/>
    </svg>
    <div class="brand">QUIVEL</div>
    <h2 class="service-title">HOME AUTOMATION</h2>
    <ul class="service-list">
      <li><svg width="16" height="16" viewBox="0 0 16 16" aria-hidden="true"><circle cx="8" cy="8" r="8" fill="var(--pink)"/><path d="M6 4.5 9.5 8 6 11.5" fill="none" stroke="#fff" stroke-width="2"/></svg>Security Camera Installation</li>
      <li><svg width="16" height="16" viewBox="0 0 16 16" aria-hidden="true"><circle cx="8" cy="8" r="8" fill="var(--pink)"/><path d="M6 4.5 9.5 8 6 11.5" fill="none" stroke="#fff" stroke-width="2"/></svg>Sink Installation</li>
      <li><svg width="16" height="16" viewBox="0 0 16 16" aria-hidden="true"><circle cx="8" cy="8" r="8" fill="var(--pink)"/><path d="M6 4.5 9.5 8 6 11.5" fill="none" stroke="#fff" stroke-width="2"/></svg>Fireplace Mounting</li>
      <li><svg width="16" height="16" viewBox="0 0 16 16" aria-hidden="true"><circle cx="8" cy="8" r="8" fill="var(--pink)"/><path d="M6 4.5 9.5 8 6 11.5" fill="none" stroke="#fff" stroke-width="2"/></svg>Chandelier Installation</li>
      <li><svg width="16" height="16" viewBox="0 0 16 16" aria-hidden="true"><circle cx="8" cy="8" r="8" fill="var(--pink)"/><path d="M6 4.5 9.5 8 6 11.5" fill="none" stroke="#fff" stroke-width="2"/></svg><span>Television &amp; Sound Bar Mounting<br>(Hidden Wires Optional)</span></li>
    </ul>
    <div class="thumbs">
      <div class="thumb" role="img" aria-label="Wall-mounted TV with hidden wiring in a living room"><span>HIDDEN WIRES</span></div>
      <div class="thumb" role="img" aria-label="Smart home devices: thermostat, camera and hub"><span>HOME AUTOMATION</span></div>
      <div class="thumb" role="img" aria-label="Television with sound bar mounted on a wall"><span>SOUNDBAR MOUNTING</span></div>
    </div>
    <div class="contact contact--phone">
      <svg width="24" height="24" viewBox="0 0 24 24" aria-hidden="true"><path d="M6.6 10.8a15 15 0 0 0 6.6 6.6l2.2-2.2a1 1 0 0 1 1-.25 11.4 11.4 0 0 0 3.6.57 1 1 0 0 1 1 1V20a1 1 0 0 1-1 1A17 17 0 0 1 3 4a1 1 0 0 1 1-1h3.5a1 1 0 0 1 1 1c0 1.25.2 2.45.57 3.57a1 1 0 0 1-.25 1z" fill="#fff"/></svg>
      <span>(555) 013-2947</span>
    </div>
    <div class="contact contact--email">
      <svg width="24" height="18" viewBox="0 0 20 16" aria-hidden="true"><rect x="1" y="1" width="18" height="14" rx="1.5" fill="none" stroke="#fff" stroke-width="1.8"/><path d="M1.5 2l8.5 7 8.5-7" fill="none" stroke="#fff" stroke-width="1.8"/></svg>
      <span>Tech@Quivel.example</span>
    </div>
  </section>

</main>
</body>
</html>
```